THC BATH BOMB PACKAGE DESIGN

Hi ,
I have a new project. I created my vision for it on an app and uploaded it for you to see.
I included the template for the box.
The front should be similar to the vision I provided, I really like how it comes together.
SIDE PANEL 1 :
INGREDIENTS: BAKING SODA, CORN STARCH, CITRIC ACID, COCOA BUTTER, MANGO BUTTER, SHEA BUTTER, KAOLIN CLAY, CASTOR OIL, COCONUT OIL, ORGANIC
THERAPEUTIC-GRADE ESSENTIAL OILS (INCLUDING BUT NOT LIMITED TO LAVANDULA ANGUSTIFOLIA (LAVENDER), MELALEUCA ALTERNIFOLIA (TEA TREE), CHAMOMILE & GERANIUM), CANNABIS OIL (THC), PURE CBD, COCO BETAINE, SODIUM LAURYL SULFOACETATE (SLSA), ISOPROPYL ALCOHOL
COLOR IS A NATURAL RESULT OF CHAMOMILE STEAM DISTILLATION.
FOR EXTERNAL USE ONLY.
WARNING: THIS PRODUCT IS FOR USE BY INDIVIDUALS 21 YRS OF
AGE OR OLDER OR BY REGISTERED QUALIFYING PATIENTS ONLY. IT IS ILLEGAL TO DRIVE A MOTOR VEHICLE WHILE UNDER THE INFLUENCE OF MARIJUANA.
WARNING : SOME PEOPLE MAY BE SENSITIVE TO ESSENTIAL OILS. SPOT TEST BEFORE USE. CONSULT WITH YOUR PHYSICIAN BEFORE
USING THIS PRODUCT ESPECIALLY IF YOU HAVE A MEDICAL CONDITION, IF YOU TAKE PRESCRIPTION MEDICATIONS OR IF YOU ARE PREGNANT OR NURSING.
(Must be outlined :)
WARNING: USE BY PREGNANT OR BREASTFEEDING WOMEN OR BY WOMEN PLANNING TO BECOME PREGNANT MAY RESULT IN FETAL INJURY, PRETERM BIRTH, LOW BIRTHWEIGHT OR DEVELOPMENTAL PROBLEMS FOR THE CHILD.
SIDE PANEL 2 :
ICONS : (I uploaded examples for use, but I'm open to what you make of them)
HANDMADE
HIGH THC
NATURAL INGREDIENTS
VEGAN
CALMING (moon)
MOISTURIZING
BEST QUALITY (diamond)
DIRECTIONS FOR USE: Get Naked. Fill the tub with
exceptionally warm water until it reaches midway.
Introduce the bomb to the water and allow it to
fully dissolve before immersing yourself into the
luxurious organic bath you've created. Soak up to
20 minutes allowing the bath to transcend the
ordinary and transport you to higher, more
abundant vibrations.
PRESERVATIVE FREE • CHEMICAL FREE
NO DYES • NO FRAGRANCES • NO JUNK
PANEL 3 (BACK SIDE) :
(at very bottom)
PRODUCED & PACKAGED BY :
MORVEN'S TULIP COMPANY
AU P 000847
WWW.FERNWAVES.INFO

```html
<!DOCTYPE html>
<html lang="en">
<head>
<meta charset="utf-8">
<title>Velora's THC Bath Bomb – Calm &amp; Sleep Box Dieline</title>
<link rel="stylesheet" href="https://fonts.googleapis.com/css2?family=Cinzel:wght@400;700&family=Montserrat:wght@400;500&family=Roboto:wght@400;700&family=Roboto+Condensed:wght@400;700&display=swap">
<style>
:root{
  --purple:#4a2a7c;
  --lavender:#e4e0ee;
  --lilac:#cfc6e4;
  --violet-glow:#9a6ac0;
  --blue-glow:#7f8fe0;
  --green:#1d8a3e;
  --green-soft:#8fc9a0;
  --red:#e0262d;
  --ink:#2b2140;
  --white:#ffffff;
  --bg:#ffffff;
}
*{box-sizing:border-box;margin:0;padding:0}
html,body{width:1200px;height:2231px;overflow:hidden;background:var(--bg)}
.canvas{position:relative;width:1200px;height:2231px}
.dieline{position:absolute;left:17px;top:632px;width:1110px;height:920px;transform:scale(1.05);transform-origin:0 0;filter:drop-shadow(0 8px 12px rgba(0,0,0,.18))}
.dieline-shapes{position:absolute;inset:0}
.panel{position:absolute;background:var(--white);overflow:hidden}
.glow{position:absolute;border-radius:50%;filter:blur(14px)}
.warning-symbol{position:absolute;border-radius:6px;background:radial-gradient(ellipse at center,var(--green) 0%,var(--green-soft) 55%,rgba(255,255,255,0) 85%)}

/* front */
.front{left:80px;top:328px;width:255px;height:237px;text-align:center}
.front .glow{left:55px;top:60px;width:160px;height:120px;background:radial-gradient(circle,var(--violet-glow) 0%,var(--blue-glow) 45%,rgba(255,255,255,0) 75%);opacity:.85}
.front .warning-symbol{left:45px;top:18px;width:34px;height:30px}
.front-copy{position:relative;padding-top:52px;color:var(--purple)}
.brand-name{font-family:"Cinzel",serif;font-weight:700;font-size:24px;color:var(--lilac);letter-spacing:1px;line-height:1}
.product-type{font-family:"Montserrat",sans-serif;font-size:8px;letter-spacing:4px;margin-top:8px}
.product-name{font-family:"Cinzel",serif;font-weight:400;font-size:19px;letter-spacing:3px;line-height:1.05;margin-top:10px}
.product-tagline{font-family:"Montserrat",sans-serif;font-size:6px;letter-spacing:2.5px;line-height:1.4;margin-top:7px;color:#8a6ab8}
.rule{width:150px;height:1px;background:#9a7ac8;margin:6px auto}
.product-extracts{font-family:"Montserrat",sans-serif;font-size:5px;letter-spacing:2px;line-height:1.45}

/* bottom + top panels */
.bottom{left:65px;top:565px;width:280px;height:255px}
.bottom .glow{left:20px;top:-40px;width:240px;height:90px;background:radial-gradient(ellipse,var(--violet-glow) 0%,var(--blue-glow) 45%,rgba(255,255,255,0) 75%)}
.bottom .warning-symbol{left:55px;top:48px;width:170px;height:150px}
.top{left:578px;top:85px;width:277px;height:255px}
.top .glow{left:20px;top:205px;width:240px;height:90px;background:radial-gradient(ellipse,var(--violet-glow) 0%,var(--blue-glow) 45%,rgba(255,255,255,0) 75%)}
.top .warning-symbol{left:62px;top:40px;width:150px;height:132px}

/* back */
.back{left:590px;top:340px;width:255px;height:228px;background:transparent}
.back-upper{position:absolute;inset:0 0 58px 0;background:var(--white);text-align:center}
.back .glow{left:15px;top:-45px;width:225px;height:80px;background:radial-gradient(ellipse,var(--violet-glow) 0%,var(--blue-glow) 45%,rgba(255,255,255,0) 75%)}
.back .warning-symbol{left:82px;top:28px;width:92px;height:81px}
.producer-label{position:absolute;left:0;right:0;bottom:6px;font-family:"Roboto",sans-serif;font-weight:700;font-size:8px;color:var(--ink)}
.producer-band{position:absolute;left:0;right:0;top:170px;height:45px;background:var(--purple);color:#e8e2f4;text-align:center;font-family:"Roboto",sans-serif;font-size:9px;line-height:1.35;padding-top:8px}
.producer-web{position:absolute;left:0;right:0;top:215px;height:13px;background:var(--white);text-align:center;font-family:"Montserrat",sans-serif;font-size:6px;letter-spacing:1.5px;color:var(--ink);padding-top:3px}

/* ingredients side */
.ingredients{left:335px;top:340px;width:255px;height:235px;background:transparent}
.ingredients-block{background:var(--lavender);padding:6px 8px 4px;font-family:"Roboto Condensed",sans-serif;font-size:6.2px;line-height:1.3;color:var(--ink)}
.ingredients-block strong{font-size:8px}
.ingredients-note{margin-top:5px;font-weight:700;font-size:6px}
.external-bar{background:var(--purple);color:var(--white);text-align:center;font-family:"Roboto Condensed",sans-serif;font-weight:700;font-size:6px;padding:2px 0}
.warnings{background:var(--white);padding:6px 8px;font-family:"Roboto Condensed",sans-serif;font-size:6.6px;line-height:1.3;color:var(--ink);height:75px}
.warnings p+p{margin-top:5px}
.warn-key{color:var(--red);font-weight:700;font-size:7.5px}
.pregnancy-warning{background:var(--purple);color:var(--white);padding:6px 8px;font-family:"Roboto Condensed",sans-serif;font-size:6.6px;line-height:1.3;height:67px}
.pregnancy-warning strong{font-size:7.5px}

/* benefits side */
.benefits{left:845px;top:340px;width:265px;height:235px;background:transparent}
.icon-grid{list-style:none;background:var(--white);height:100px;padding:8px 12px;display:grid;grid-template-columns:1fr 1fr;row-gap:7px;align-content:start}
.icon-item{display:flex;align-items:center;gap:6px;font-family:"Roboto Condensed",sans-serif;font-weight:700;font-size:7.5px;color:var(--ink)}
.icon-item small{font-size:4px;font-weight:400}
.icon-dot{width:15px;height:15px;border-radius:50%;background:var(--purple);border:2px solid #b8a6d8;flex:none}
.directions{background:var(--lavender);height:70px;padding:5px 12px;font-family:"Roboto Condensed",sans-serif;font-size:6.3px;line-height:1.25;color:var(--ink)}
.directions strong{font-size:7.5px}
.claims{background:var(--purple);height:65px;padding-top:8px;text-align:center;color:#e8e2f4;font-family:"Roboto",sans-serif;font-size:8.5px;line-height:1.4}
.claims strong{color:var(--white)}
</style>
</head>
<body>
<main class="canvas">
  <section class="dieline" aria-label="Bath bomb box dieline">
    <svg class="dieline-shapes" width="1110" height="920" viewBox="0 0 1110 920" aria-hidden="true">
      <g fill="#4a2a7c">
        <path d="M578 85 V58 Q578 8 628 8 H805 Q855 8 855 58 V85 Z"/>
        <path d="M5 345 L80 328 V565 L5 548 Z"/>
        <path d="M65 820 H345 V860 Q345 910 295 910 H115 Q65 910 65 860 Z"/>
        <rect x="65" y="810" width="280" height="12"/>
        <path d="M360 205 H590 V340 H325 V255 Z"/>
        <path d="M335 575 H590 V620 L565 700 H335 Z"/>
        <path d="M845 205 H1075 L1110 255 V340 H845 Z"/>
        <path d="M845 575 H1110 V700 H870 L845 620 Z"/>
      </g>
    </svg>

    <div class="panel front">
      <div class="glow"></div>
      <div class="warning-symbol" role="img" aria-label="Small regulatory marijuana product warning symbol"></div>
      <div class="front-copy">
        <h1 class="brand-name">VELORA'S</h1>
        <p class="product-type">THC BATH BOMB</p>
        <h2 class="product-name">CALM &amp;<br>SLEEP</h2>
        <p class="product-tagline">RELAXING RELIEF FOR<br>MIND &amp; BODY</p>
        <div class="rule"></div>
        <p class="product-extracts">WITH AROMATHERAPEUTIC<br>PLANT EXTRACTS<br>CHAMOMILE ♡ LAVENDER<br>• GERANIUM • TEA TREE •<br>FRANKINCENSE &amp; HELICHRYSUM</p>
      </div>
    </div>

    <div class="panel bottom">
      <div class="glow"></div>
      <div class="warning-symbol" role="img" aria-label="Regulatory marijuana product warning symbol"></div>
    </div>

    <div class="panel top">
      <div class="glow"></div>
      <div class="warning-symbol" role="img" aria-label="Regulatory marijuana product warning symbol"></div>
    </div>

    <div class="panel back">
      <div class="back-upper">
        <div class="glow"></div>
        <div class="warning-symbol" role="img" aria-label="Regulatory marijuana product warning symbol"></div>
        <p class="producer-label">PRODUCED &amp; PACKAGED BY :</p>
      </div>
      <div class="producer-band">MORVEN'S TULIP COMPANY<br>AU P 000847</div>
      <div class="producer-web">www.fernwaves.info</div>
    </div>

    <div class="panel ingredients">
      <div class="ingredients-block">
        <p><strong>INGREDIENTS:</strong> Baking Soda, Corn Starch, Citric Acid, Cocoa Butter, Mango Butter, Shea Butter, Kaolin Clay, Castor Oil, Coconut Oil, Organic Therapeutic-grade Essential Oils (Including But Not Limited To Lavandula Angustifolia (Lavender), Melaleuca Alternifolia (Tea Tree), Chamomile &amp; Geranium), Cannabis Oil (Thc), Pure Cbd, Coco Betaine, Sodium Lauryl Sulfoacetate (Slsa), Isopropyl Alcohol</p>
        <p class="ingredients-note">COLOR IS A NATURAL RESULT OF CHAMOMILE STEAM DISTILLATION.</p>
      </div>
      <div class="external-bar">FOR EXTERNAL USE ONLY.</div>
      <div class="warnings">
        <p><span class="warn-key">WARNING:</span> This Product Is For Use By Individuals 21 Yrs Of Age Or Older Or By Registered Qualifying Patients Only. It Is Illegal To Drive A Motor Vehicle While Under The Influence Of Marijuana.</p>
        <p><span class="warn-key">WARNING:</span> Some People May Be Sensitive To Essential Oils. Spot Test Before Use. Consult With Your Physician Before Using This Product Especially If You Have A Medical Condition, If You Take Prescription Medications Or If You Are Pregnant Or Nursing.</p>
      </div>
      <div class="pregnancy-warning">
        <p><strong>WARNING:</strong> Use By Pregnant Or Breastfeeding Women Or By Women Planning To Become Pregnant May Result In Fetal Injury, Preterm Birth, Low Birthweight Or Developmental Problems For The Child.</p>
      </div>
    </div>

    <div class="panel benefits">
      <ul class="icon-grid">
        <li class="icon-item"><span class="icon-dot"></span>HANDMADE</li>
        <li class="icon-item"><span class="icon-dot"></span>CALMING <small>(moon)</small></li>
        <li class="icon-item"><span class="icon-dot"></span>HIGH THC</li>
        <li class="icon-item"><span class="icon-dot"></span>MOISTURIZING</li>
        <li class="icon-item"><span class="icon-dot"></span>NATURAL INGREDIENTS</li>
        <li class="icon-item"><span class="icon-dot"></span>BEST QUALITY <small>(diamond)</small></li>
        <li class="icon-item"><span class="icon-dot"></span>VEGAN</li>
      </ul>
      <div class="directions">
        <p><strong>DIRECTIONS FOR USE:</strong> Get Naked. Fill The Tub With Exceptionally Warm Water Until It Reaches Midway. Introduce The Bomb To The Water And Allow It To Fully Dissolve Before Immersing Yourself Into The Luxurious Organic Bath You've Created. Soak Up To 20 Minutes Allowing The Bath To Transcend The Ordinary And Transport You To Higher, More Abundant Vibrations.</p>
      </div>
      <div class="claims">
        <p>PRESERVATIVE FREE</p>
        <p><strong>• CHEMICAL FREE NO DYES &nbsp;• NO FRAGRANCES<br>• NO JUNK</strong></p>
      </div>
    </div>
  </section>
</main>
</body>
</html>
```